Halloway Crest Backers Guild business cards

Create a single-sided business card for the Halloway Crest Backers Guild based on the attached logo.
The additional data fields include Name, Title, Email, Phone, and website.
Please use the following as sample data:
Name: Dean Varrow
Title: Co-Founder / Investor
Email: deanvarrow@mailtern.net
Phone: 555-314-2706
Website: www.hcbackersguild.com

Target Market(s)

Start ups, entrepreneurs, venture capitalists

Industry/Entity Type

Investment

Contact Information for Business Card

Professional business card. Technology company.

Font styles to use
Serif
Sans Serif

Requirements
Must have
• Include the HCBG logo (attached)
• Name
• Title
• Email
• Phone
• Website
Should not have
• Cute, cartoony

```html
<!DOCTYPE html>
<html lang="en">
<head>
<meta charset="utf-8">
<title>Halloway Crest Backers Guild – Business Cards</title>
<link rel="stylesheet" href="https://fonts.googleapis.com/css2?family=Open+Sans:wght@400;600;700&display=swap">
<style>
  :root {
    --green: #1aa862;
    --green-light: #1fbd73;
    --ink: #4a4a4a;
    --ink-soft: #5c5c5c;
    --card: #f7f7f7;
    --card-edge: #e6e6e6;
    --backdrop: #d9d6d0;
  }
  * { box-sizing: border-box; margin: 0; padding: 0; }
  html, body {
    width: 1200px; height: 1023px; overflow: hidden;
    background: var(--backdrop);
    font-family: "Open Sans", Arial, sans-serif;
  }
  .canvas { position: relative; width: 1200px; height: 1023px; }

  .card {
    position: absolute;
    width: 620px; height: 354px;
    border-radius: 18px;
    background: linear-gradient(160deg, #ffffff 0%, var(--card) 60%, #ececec 100%);
    box-shadow: 0 2px 0 var(--card-edge), 0 14px 30px rgba(0,0,0,0.18);
    overflow: hidden;
  }

  /* Front */
  .card-front { left: 60px; top: 90px; }
  .brand {
    position: absolute; left: 70px; top: 96px;
    display: flex; align-items: center; gap: 22px;
  }
  .brand-dot { width: 34px; height: 34px; border-radius: 50%; background: var(--green); flex: none; }
  .brand-rule { width: 1px; height: 96px; background: var(--green); opacity: .6; flex: none; }
  .brand-name {
    font-size: 34px; font-weight: 600; line-height: 1.2;
    color: var(--ink); letter-spacing: .5px;
  }
  .front-band {
    position: absolute; left: 0; right: 0; bottom: 0; height: 62px;
    background: var(--green);
    display: flex; align-items: center; justify-content: flex-end;
    padding-right: 34px;
  }
  .front-band .web { color: #fff; font-size: 17px; letter-spacing: .5px; }

  /* Back */
  .card-back { left: 520px; top: 560px; }
  .name-tab {
    position: absolute; left: 0; top: 0;
    width: 290px; height: 96px;
    background: var(--green-light);
    border-radius: 0 0 48px 0;
    padding: 16px 0 0 30px;
    color: #fff;
  }
  .name-tab .person { font-size: 26px; font-weight: 600; }
  .name-tab .role { font-size: 14px; color: #0d6b3d; margin-top: 2px; }
  .contacts {
    position: absolute; left: 30px; top: 122px;
    list-style: none;
  }
  .contacts li {
    display: flex; align-items: center; gap: 14px;
    font-size: 18px; color: var(--ink-soft);
    height: 34px;
  }
  .contacts svg { width: 18px; height: 18px; flex: none; }
  .back-brand {
    position: absolute; right: 30px; bottom: 34px;
    display: flex; align-items: center; gap: 12px;
  }
  .back-brand .brand-dot { width: 20px; height: 20px; }
  .back-brand .brand-rule { height: 52px; }
  .back-brand .brand-name { font-size: 18px; }
</style>
</head>
<body>
<div class="canvas">

  <section class="card card-front">
    <div class="brand">
      <span class="brand-dot"></span>
      <span class="brand-rule"></span>
      <div class="brand-name">Halloway Crest<br>Backers Guild</div>
    </div>
    <div class="front-band"><span class="web">www.hcbackersguild.com</span></div>
  </section>

  <section class="card card-back">
    <div class="name-tab">
      <div class="person">Dean Varrow</div>
      <div class="role">Co-Founder / Investor</div>
    </div>
    <ul class="contacts">
      <li>
        <svg viewBox="0 0 20 20" aria-hidden="true"><path d="M10 1a6 6 0 0 0-6 6c0 5 6 12 6 12s6-7 6-12a6 6 0 0 0-6-6z" fill="var(--green)"/><circle cx="10" cy="7" r="2.2" fill="#fff"/></svg>
        Your address
      </li>
      <li>
        <svg viewBox="0 0 20 20" aria-hidden="true"><circle cx="10" cy="10" r="8.5" fill="none" stroke="var(--green)" stroke-width="1.6"/><path d="M7.5 6.5l1.5-.5 1 2-1 1c.5 1 1.3 1.8 2.2 2.2l1-1 2 1-.5 1.5c-3 .3-6.4-3-6.2-6.2z" fill="var(--green)"/></svg>
        555-314-2706
      </li>
      <li>
        <svg viewBox="0 0 20 20" aria-hidden="true"><rect x="2" y="4.5" width="16" height="11" fill="none" stroke="var(--green)" stroke-width="1.6"/><path d="M2 4.5l8 6 8-6" fill="none" stroke="var(--green)" stroke-width="1.6"/></svg>
        deanvarrow@mailtern.net
      </li>
      <li>
        <svg viewBox="0 0 20 20" aria-hidden="true"><g fill="none" stroke="var(--green)" stroke-width="1.5"><circle cx="10" cy="10" r="8.5"/><ellipse cx="10" cy="10" rx="3.8" ry="8.5"/><path d="M1.5 10h17M3 5.5h14M3 14.5h14"/></g></svg>
        www.hcbackersguild.com
      </li>
    </ul>
    <div class="back-brand">
      <span class="brand-dot"></span>
      <span class="brand-rule"></span>
      <div class="brand-name">Halloway Crest<br>Backers Guild</div>
    </div>
  </section>

</div>
</body>
</html>
```